New business card with our logo

we finalized our logo with the help of pixel harbor - now we need a business card using that logo. we are a metal service center providing raw steel and metal products for fabricating, contractors, artists, etc. we have the wording for the back of the card figured out (attached, no deviations from text please), just need help putting it all together.
Contact Information for Business Card
would like the look of steel somehow incorporated in the design ... would like the black part of the logo to be steel or silver color (the S & MORROW)
Font styles to use
Other font styles liked:
- calibri, arial, similar to those, modern looking
Colors
Designer to choose colors to be used in the design.
Requirements
Must have
- Back of card must haves are attached (no deviations from wording please).
- FRONT of card:
- logo
- address
- name
- office tel
- cell
- fax
- website
- address
Nice to have
- incorporate the look of steel or element of steel somehow
- names of the staff on front not in all caps, i.e. Tereza not TEREZA
- this industry is more industrial, not coffee or flower shop so design should be aligned with that
- design should be classic and tasteful

```html
<!DOCTYPE html>
<html lang="en">
<head>
<meta charset="utf-8">
<title>Morrow Steel – Business Card</title>
<link href="https://fonts.googleapis.com/css2?family=Lato:ital,wght@0,400;0,700;0,900;1,700;1,900&display=swap" rel="stylesheet">
<style>
  :root {
    --page: #e9e9ea;
    --card-dark: #2b2c2e;
    --card-light: #fbfbfb;
    --steel-blue: #1a6fc0;
    --ink: #2a2b2d;
    --ink-soft: #4a4b4e;
    --white: #ffffff;
    --rule-grey: #9a9a9c;
  }
  * { margin: 0; padding: 0; box-sizing: border-box; }
  html, body { width: 1200px; height: 715px; overflow: hidden; }
  body {
    background: var(--page);
    font-family: "Lato", Arial, sans-serif;
    position: relative;
  }
  .card {
    position: absolute;
    top: 209px;
    width: 520px;
    height: 297px;
    border-radius: 3px;
    box-shadow: 0 6px 18px rgba(0,0,0,.18);
    overflow: hidden;
  }

  /* Back of card */
  .card-back { left: 50px; background: var(--card-dark); color: var(--white); text-align: center; }
  .wordmark {
    font-weight: 900;
    font-size: 34px;
    letter-spacing: 1px;
    display: flex; align-items: center; justify-content: center; gap: 12px;
  }
  .wordmark .dot {
    width: 30px; height: 30px; border-radius: 50%;
    border: 3px solid currentColor;
  }
  .card-back .wordmark { color: var(--steel-blue); margin-top: 30px; }
  .tagline {
    font-weight: 900; font-style: italic; font-size: 26px;
    margin-top: 14px; letter-spacing: .5px;
  }
  .tagline-rule { width: 300px; height: 2px; background: var(--steel-blue); margin: 6px auto 0; }
  .services {
    display: inline-block;
    background: var(--white); color: var(--steel-blue);
    font-size: 12px; letter-spacing: .5px;
    padding: 4px 12px; margin-top: 10px;
  }
  .services .sep { color: var(--ink); }
  .products { font-size: 14px; line-height: 1.35; margin-top: 10px; color: #e8e8e8; }
  .delivery-band {
    position: absolute; left: 0; right: 0; bottom: 0; height: 46px;
    background: var(--white); color: var(--ink);
    font-weight: 900; font-style: italic; font-size: 14px;
    display: flex; align-items: center; justify-content: center;
  }

  /* Front of card */
  .card-front { left: 630px; background: var(--card-light); color: var(--ink); }
  .card-front .wordmark { color: var(--ink); margin-top: 52px; }
  .details { position: absolute; left: 0; right: 0; top: 160px; display: flex; }
  .person { width: 228px; text-align: right; padding-right: 22px; font-size: 14px; }
  .person .name { font-size: 15px; }
  .person .name b { color: var(--steel-blue); font-weight: 700; }
  .person .role { color: var(--ink-soft); font-size: 13px; }
  .person .address { font-weight: 900; margin-top: 12px; line-height: 1.3; }
  .divider {
    width: 2px; height: 100px;
    background: linear-gradient(to bottom, transparent, var(--rule-grey) 30%, var(--ink) 70%, transparent);
  }
  .contact { list-style: none; padding-left: 22px; font-size: 13.5px; line-height: 1.75; padding-top: 8px; }
  .contact li { display: flex; align-items: center; gap: 10px; }
  .contact svg { width: 12px; height: 12px; fill: var(--steel-blue); flex: none; }
</style>
</head>
<body>

<section class="card card-back" aria-label="Back of business card">
  <div class="wordmark"><span class="dot"></span>MORROW STEEL</div>
  <div class="tagline">METAL SERVICE CENTER</div>
  <div class="tagline-rule"></div>
  <div class="services">CUT <span class="sep">•</span> SHEAR <span class="sep">•</span> PUNCH <span class="sep">•</span> LIGHT FAB</div>
  <p class="products">Structural Steel, Stainless &amp; Aluminum,<br>Building Components, Rebar, Decking.. &amp; more..</p>
  <div class="delivery-band">CUT TO SIZE, PICK-UP OR DELIVERED !</div>
</section>

<section class="card card-front" aria-label="Front of business card">
  <div class="wordmark"><span class="dot"></span>MORROW STEEL</div>
  <div class="details">
    <div class="person">
      <div class="name">Daniel <b>Okafor</b></div>
      <div class="role">Director</div>
      <div class="address">48 Foundry Lane,<br>Eastbrook</div>
    </div>
    <div class="divider"></div>
    <ul class="contact">
      <li><svg viewBox="0 0 12 12"><path d="M1 4c0-2 2-3 5-3s5 1 5 3l-2 1-1-2H4L3 5zM2 6h8l1 5H1z"/></svg>512.555.0142</li>
      <li><svg viewBox="0 0 12 12"><path d="M3 1h6v3H3zM1 5h10v4H9v2H3V9H1zM4 8v2h4V8z"/></svg>512.555.0187</li>
      <li><svg viewBox="0 0 12 12"><path d="M1 2h10v8H1zM2 3l4 3 4-3z" fill-rule="evenodd"/></svg>daniel@morrowsteel.example</li>
      <li><svg viewBox="0 0 12 12"><circle cx="6" cy="6" r="5"/></svg>www.morrowsteel.example</li>
    </ul>
  </div>
</section>

</body>
</html>
```